Renaldo's Motorworks landing page to Dealership page, Rental Car Page, and Auto Body page.

I'm looking for my website to have RenaldosMotor.com be the landing page. From there visitors will have the option to visit three pages. My auto dealer page, of which I will provide an example of how I'd like it done. Auto body page, where I will fill in the text. The rental car page. Basically on the auto dealer and rental page I'll need the ability to add vehicles and delete as I need. Otherwise, its a pretty straightforward site. Nothing extensive. I already have the logo design from a previous project on here completed and can provide. If more funded needed for page capabilities, I can provide. I do have an account with HostPeak, with renaldosmotor.com already under them.

Target Market(s)

Automotive

Industry/Entity Type

Auto body repair, dealership, rental car.

Coding

Coded - Design and coding required

Number of Pages Required

4 page

Font styles to use
Sans Serif

Colors
0054AA
0677BA
7BADD7
CADEEF
E8F1F8

Requirements
Must have
• My logo Renaldos Motorworks at the top. Be creative with pics in the background of cars.
Nice to have
• Ease of use with being able to add vehicles for sale, and rental cars.
Should not have
• Nothing complex, would like to get in and out. Nothing to extensive on the designs of the pages, simple but attractive.

```html
<!DOCTYPE html>
<html lang="en">
<head>
<meta charset="utf-8">
<title>Renaldo's Motorworks</title>
<link href="https://fonts.googleapis.com/css2?family=Rubik:wght@300;400;500;700&display=swap" rel="stylesheet">
<style>
:root{
  --blue:#0677BA;
  --blue-deep:#0054AA;
  --blue-soft:#7BADD7;
  --blue-pale:#CADEEF;
  --blue-mist:#E8F1F8;
  --ink:#1d1d1f;
  --text:#333;
  --white:#fff;
}
*{margin:0;padding:0;box-sizing:border-box}
html,body{width:1200px;height:2782px;overflow:hidden;background:var(--white)}
body{position:relative;font-family:"Rubik",sans-serif;color:var(--text)}
.abs{position:absolute}

/* hero */
.hero{left:0;top:0;width:1200px;height:660px;
  background:
    radial-gradient(ellipse 420px 260px at 880px 380px,rgba(190,192,197,.85) 0%,rgba(150,152,158,.55) 55%,rgba(150,152,158,0) 100%),
    linear-gradient(180deg,#f8e6c4 0%,#f3cd98 30%,#c39f7c 50%,#6a5645 70%,#2e2a26 100%);}
.torn-bottom{left:0;top:590px;width:1200px;height:72px}
.phone-tab{left:728px;top:0;width:302px;height:45px;background:#2b2b2b;
  clip-path:polygon(0 0,100% 0,92% 100%,8% 100%);
  display:flex;align-items:center;justify-content:center;gap:12px;color:var(--white);font-weight:700;font-size:14.5px}
.phone-tab svg{width:28px;height:28px}
.brand{left:162px;top:78px;display:flex;align-items:center;gap:10px}
.brand-dot{width:26px;height:26px;border-radius:50%;background:var(--blue)}
.brand-name{font-weight:700;font-size:25px;line-height:1.05;color:var(--ink);width:170px}
.hero-title{left:158px;top:222px;font-size:50px;line-height:58px;color:var(--ink)}
.hero-title strong{display:block;font-weight:700;color:var(--blue)}
.hero-title span{display:block;font-weight:300}
.hero-copy{left:160px;top:347px;width:360px;font-size:14.5px;line-height:29px;color:#111}
.btn{display:flex;align-items:center;justify-content:center;background:var(--blue);color:var(--white);font-size:13px;letter-spacing:.2px;text-decoration:none}
.hero-btn{left:182px;top:432px;width:178px;height:44px;font-size:16px}

/* feature rows */
.photo{position:absolute}
.splash{position:absolute;border-radius:50%;background:radial-gradient(circle,rgba(123,173,215,.75) 0%,rgba(123,173,215,.35) 50%,rgba(123,173,215,0) 72%)}
.splash-grey{background:radial-gradient(circle,rgba(169,180,194,.8) 0%,rgba(169,180,194,.35) 50%,rgba(169,180,194,0) 72%)}
.feature-title{font-size:33px;line-height:40px;color:var(--ink)}
.feature-title strong{display:block;font-weight:700;color:var(--blue)}
.feature-title span{display:block;font-weight:300;font-size:24px;line-height:32px;margin-top:6px}
.feature-copy{width:350px;font-size:14.5px;line-height:24px;color:#444;margin-top:22px}
.link-line{height:1px;background:var(--blue)}
.feature-btn{width:205px;height:43px}

/* footer */
.footer{left:0;top:2340px;width:1200px;height:442px;background:linear-gradient(180deg,#1b1b1b,#2f2f2f 60%,#262626)}
.torn-top{left:0;top:2340px;width:1200px;height:70px}
.f-brand{left:157px;top:2478px;display:flex;align-items:center;gap:8px}
.f-brand .brand-dot{width:18px;height:18px;background:var(--white)}
.f-brand .brand-name{font-size:16px;color:var(--white);width:110px}
.f-about{left:156px;top:2553px;width:200px;font-size:11.5px;line-height:17px;color:#ddd}
.f-head{font-size:16px;font-weight:500;color:var(--white)}
.f-list{list-style:none;margin-top:20px;font-size:12.5px;color:#eee}
.f-address li{display:flex;align-items:center;gap:14px;height:45px}
.f-address svg{width:16px;height:16px;stroke:#ddd;fill:none;stroke-width:1.4}
.f-links li{height:32px;line-height:22px}
.social{display:flex;gap:9px;margin-top:20px}
.social i{width:25px;height:25px;border:1.4px solid #eee;border-radius:50%}
.copyright{left:0;top:2710px;width:1200px;text-align:center;font-size:11.5px;color:#eee}
</style>
</head>
<body>

<!-- hero -->
<div class="abs hero" role="img" aria-label="Silver coupe parked on a roadside at sunset"></div>
<svg class="abs torn-bottom" viewBox="0 0 1200 72" preserveAspectRatio="none">
  <path fill="#fff" d="M0 18 L40 28 L80 22 L120 34 L160 26 L200 38 L240 30 L280 44 L320 40 L360 52 L400 46 L440 58 L480 50 L520 60 L560 54 L600 62 L640 55 L680 64 L720 52 L760 58 L800 48 L840 56 L880 44 L920 50 L960 38 L1000 44 L1040 30 L1080 36 L1120 24 L1160 30 L1200 20 L1200 72 L0 72Z"/>
</svg>
<div class="abs phone-tab">
  <svg viewBox="0 0 28 28"><circle cx="14" cy="14" r="12.5" fill="none" stroke="#fff" stroke-width="1.6"/><path d="M10 8.5c.8-.6 1.6-.3 2 .5l1 2c.3.7 0 1.2-.5 1.6l-.6.5c.6 1.4 1.6 2.4 3 3l.5-.6c.4-.5 1-.8 1.6-.5l2 1c.8.4 1.1 1.2.5 2-1 1.3-2.6 1.7-4.3.8-2.6-1.3-4.6-3.3-5.9-5.9-.9-1.7-.5-3.3.7-4.4z" fill="#fff"/></svg>
  <span>000 555 0142 318</span>
</div>
<div class="abs brand"><i class="brand-dot"></i><span class="brand-name">RENALDO'S MOTORWORKS</span></div>
<h1 class="abs hero-title"><strong>BEST CAR FOR</strong><span>RENT TODAY</span></h1>
<p class="abs hero-copy">Lorem ipsum dolor sit amet, consectetur adipiscing elit, eiusmod tempor incididunt ut labore</p>
<a class="abs btn hero-btn">OUR SERVICES</a>

<!-- feature 1 -->
<div class="photo" style="left:0;top:760px;width:620px;height:500px;background:radial-gradient(ellipse 220px 200px at 400px 250px,#b9bcc1 0%,#8f9399 45%,rgba(143,147,153,0) 100%),linear-gradient(180deg,#2d4157 0%,#1e3550 50%,#132840 100%)" role="img" aria-label="Car engine with brake disc in front of a night city skyline"></div>
<div class="splash" style="left:430px;top:720px;width:130px;height:150px" role="img" aria-label="Blue paint splash"></div>
<div class="abs" style="left:673px;top:820px">
  <h2 class="feature-title"><strong>25% OFF FOR</strong><span>AUTO CAR SERVICES</span></h2>
  <p class="feature-copy">Over hundreds of brands and tens of thousands of parts Select Year. Lorem ipsum dolor sit amet, con-sectetur adipiscing elit, eiusmod tempor</p>
</div>
<div class="abs link-line" style="left:620px;top:1041px;width:60px"></div>
<a class="abs btn feature-btn" style="left:680px;top:1019px">AUTO BODY REPAIR</a>
<div class="splash" style="left:1110px;top:840px;width:140px;height:240px" role="img" aria-label="Blue paint splash"></div>

<!-- feature 2 -->
<div class="photo" style="left:560px;top:1228px;width:640px;height:500px;background:radial-gradient(ellipse 260px 140px at 280px 300px,#ff9a2a 0%,#f07d10 45%,rgba(240,125,16,0) 100%),linear-gradient(180deg,#1a2230 0%,#2c3442 40%,#3a3f48 70%,#22252b 100%)" role="img" aria-label="Orange sports car on a rainy night street"></div>
<div class="splash splash-grey" style="left:612px;top:1255px;width:120px;height:145px" role="img" aria-label="Grey paint splash"></div>
<div class="abs" style="left:157px;top:1383px">
  <h2 class="feature-title"><strong>GET THE BEST</strong><span>CAR DEALS</span></h2>
  <p class="feature-copy">Over hundreds of brands and tens of thousands of parts Select Year. Lorem ipsum dolor sit amet, con-sectetur adipiscing elit, eiusmod tempor</p>
</div>
<div class="abs link-line" style="left:368px;top:1594px;width:192px"></div>
<a class="abs btn feature-btn" style="left:163px;top:1573px">AUTO DEALER</a>

<!-- feature 3 -->
<div class="photo" style="left:0;top:1795px;width:620px;height:500px;background:radial-gradient(ellipse 250px 130px at 370px 330px,#2f62c4 0%,#1d4aa6 45%,rgba(29,74,166,0) 100%),linear-gradient(180deg,#5a3c22 0%,#3a2a1d 40%,#2a1f18 75%,#1b1512 100%)" role="img" aria-label="Blue convertible in front of a steel bridge at dusk"></div>
<div class="splash" style="left:445px;top:1830px;width:170px;height:150px" role="img" aria-label="Blue paint splash"></div>
<div class="abs" style="left:673px;top:1856px">
  <h2 class="feature-title"><strong>WEEKLY &amp; MONTHLY</strong><span>CAR RENTAL SERVICES</span></h2>
  <p class="feature-copy">Over hundreds of brands and tens of thousands of parts Select Year. Lorem ipsum dolor sit amet, con-sectetur adipiscing elit, eiusmod tempor</p>
</div>
<div class="abs link-line" style="left:620px;top:2061px;width:60px"></div>
<a class="abs btn feature-btn" style="left:680px;top:2040px">CAR RENTAL</a>
<div class="splash" style="left:1115px;top:1965px;width:130px;height:150px" role="img" aria-label="Blue paint splash"></div>

<!-- footer -->
<footer>
<div class="abs footer" role="img" aria-label="Dark evening scene with a parked SUV"></div>
<svg class="abs torn-top" viewBox="0 0 1200 70" preserveAspectRatio="none">
  <path fill="#fff" d="M0 0 L1200 0 L1200 50 L1160 44 L1120 30 L1080 36 L1040 22 L1000 30 L960 20 L920 28 L880 16 L840 24 L800 18 L760 30 L720 22 L680 34 L640 26 L600 40 L560 32 L520 42 L480 34 L440 46 L400 40 L360 50 L320 42 L280 52 L240 46 L200 56 L160 48 L120 58 L80 54 L40 62 L0 56Z"/>
</svg>
<div class="abs f-brand"><i class="brand-dot"></i><span class="brand-name">RENALDO'S MOTORWORKS</span></div>
<p class="abs f-about">Lorem ipsum dolor sit amet, consecte-tur adipiscing elit. Quisque pharetra condimentum.</p>

<div class="abs" style="left:412px;top:2455px">
  <h3 class="f-head">Our Address</h3>
  <ul class="f-list f-address">
    <li><svg viewBox="0 0 16 16"><path d="M8 15s5-5 5-9a5 5 0 0 0-10 0c0 4 5 9 5 9z"/><circle cx="8" cy="6" r="2"/></svg>418 Larkmoor Ave, Brookfield</li>
    <li><svg viewBox="0 0 16 16"><path d="M3 2l3 .5 1 3-1.5 1.5a8 8 0 0 0 4 4L11 9.5l3 1 .5 3c-6 1-12-5-11.5-11.5z"/></svg>+1 555 010 2299</li>
    <li><svg viewBox="0 0 16 16"><rect x="1.5" y="3.5" width="13" height="9"/><path d="M1.5 3.5 8 9l6.5-5.5"/></svg>hello@renaldosmotor.com</li>
    <li><svg viewBox="0 0 16 16"><circle cx="8" cy="8" r="6.5"/><path d="M8 4v4l3 2"/></svg>09.00 - 17.00</li>
  </ul>
</div>
<div class="abs" style="left:660px;top:2455px">
  <h3 class="f-head">Quick Links</h3>
  <ul class="f-list f-links">
    <li>Home</li><li>Dealership</li><li>Car Rental</li><li>Auto Body</li><li>Contact us</li>
  </ul>
</div>
<div class="abs" style="left:872px;top:2455px">
  <h3 class="f-head">Follow Us</h3>
  <div class="social"><i></i><i></i><i></i><i></i></div>
</div>
<p class="abs copyright">Copyright © 2021 RenaldosMotor.com.</p>
</footer>

</body>
</html>
```